Vellmore Quadrant Systems LLC
Elevate Your Workflow
Vellmore Quadrant Systems LLC - Information Technology
Creative Brief
Corporate
Dorian Feltcher
President
Harlow Springs, OR
dorian@vellmore-quadrant.example
www.vellmore-quadrant.example
Elevate Your Workflow www.vellmore-quadrant.example

```html
<!DOCTYPE html>
<html lang="en">
<head>
<meta charset="utf-8">
<title>Vellmore Quadrant Systems LLC — Business Card</title>
<link href="https://fonts.googleapis.com/css2?family=Open+Sans:ital,wght@0,400;0,600;0,700;0,800;1,400&display=swap" rel="stylesheet">
<style>
  :root {
    --backdrop: #e9e6e3;
    --card: #ffffff;
    --ink: #2b2b2b;
    --ink-soft: #6b6b6b;
    --cyan: #1fb3dc;
    --cyan-deep: #0e9ac4;
    --cyan-pale: #cdeef8;
    --navy: #1c2a3a;
  }
  html, body {
    margin: 0;
    width: 1200px;
    height: 897px;
    overflow: hidden;
    background: var(--backdrop);
    font-family: "Open Sans", sans-serif;
  }
  .card {
    position: absolute;
    left: 150px;
    top: 191px;
    width: 900px;
    height: 515px;
    background: var(--card);
    border-radius: 34px;
    overflow: hidden;
    box-shadow: 0 10px 30px rgba(0,0,0,0.18);
  }
  .card-wave {
    position: absolute;
    left: 0;
    bottom: 0;
    width: 900px;
    height: 300px;
  }
  .brand {
    position: absolute;
    left: 70px;
    top: 150px;
    display: flex;
    align-items: center;
    gap: 16px;
  }
  .brand-square {
    width: 58px;
    height: 58px;
    background: var(--cyan);
    border-radius: 6px;
  }
  .brand-name {
    font-size: 26px;
    font-weight: 800;
    color: var(--navy);
    line-height: 1.05;
    width: 270px;
  }
  .brand-tagline {
    position: absolute;
    left: 144px;
    top: 222px;
    font-size: 13px;
    font-style: italic;
    color: var(--ink-soft);
  }
  .person {
    position: absolute;
    right: 80px;
    top: 120px;
    text-align: right;
  }
  .person-name {
    font-size: 34px;
    font-weight: 700;
    color: var(--ink);
    margin: 0;
  }
  .person-title {
    font-size: 17px;
    color: var(--ink-soft);
    margin: 4px 0 0;
  }
  .contact {
    position: absolute;
    left: 144px;
    top: 290px;
    font-size: 13px;
    line-height: 1.6;
    color: var(--ink-soft);
  }
  .contact .label {
    color: var(--cyan-deep);
    font-weight: 700;
    margin-right: 4px;
  }
  .website {
    position: absolute;
    right: 80px;
    top: 232px;
    font-size: 17px;
    font-weight: 600;
    color: var(--cyan-deep);
    white-space: nowrap;
    transform: rotate(-20deg);
    transform-origin: right center;
  }
</style>
</head>
<body>
  <div class="card">
    <svg class="card-wave" viewBox="0 0 900 300" aria-hidden="true">
      <path d="M0 300 L0 255 C250 250 560 190 900 40 L900 300 Z" fill="var(--cyan-pale)"/>
      <path d="M0 300 L0 275 C260 275 580 220 900 95 L900 300 Z" fill="var(--cyan)"/>
      <path d="M0 300 L0 290 C280 292 600 250 900 140 L900 300 Z" fill="var(--cyan-deep)"/>
    </svg>

    <div class="brand">
      <div class="brand-square"></div>
      <div class="brand-name">Vellmore Quadrant Systems LLC</div>
    </div>
    <div class="brand-tagline">Elevate Your Workflow</div>

    <div class="person">
      <p class="person-name">Dorian Feltcher</p>
      <p class="person-title">President</p>
    </div>

    <div class="contact">
      1234 Birchwood Ln.<br>
      Harlow Springs, OR 99999<br>
      <span class="label">P:</span>(999) 999-9999<br>
      <span class="label">F:</span>(999) 999-9999<br>
      <span class="label">E:</span>dorian@vellmore-quadrant.example
    </div>

    <div class="website">www.vellmore-quadrant.example</div>
  </div>
</body>
</html>
```